Prestige Car Bodyshop Business Card

We are a car bodyshop based in the UK. Our customer base is mainly prestige high-value vehicles. I am looking for a classy and stylish business card design for my staff to give out to customers, with their direct email and phone number, as well as our main email and phone number with address details

I am also looking to have a general business card design with just our main company address and contact details, but also have a space to add a manufacturer approval logo (i.e Velmora, Orek, Tovalo etc... logo) in the corner somewhere.

I do not particularly want any outlines or pictures of cars on the card, I would just like a quality high-end look.

Please feel free to get in touch if you have any questions or queries?

Many Thanks

Malcolm

Target Market(s)

Prestige vehicle owners

Industry/Entity Type

Automotive

Contact Information for Business Card

I am looking for a classy and stylish business card design for my staff to give out to customers, with their direct email and phone number, as well as our main email and phone number with address details

Font styles to use
Sans Serif

Colors

Designer to choose colors to be used in the design.

Requirements
Nice to have
• I do not particularly want any outlines or pictures of cars on the card, I would just like a quality high-end look.

```html
<!DOCTYPE html>
<html lang="en">
<head>
<meta charset="utf-8">
<title>RK Halden Accident Repair Centre – Business Cards</title>
<link rel="stylesheet" href="https://fonts.googleapis.com/css2?family=Lato:wght@300;400;700&family=Arimo:wght@400&display=swap">
<style>
  :root{
    --page:#e9e7e3;
    --card-black:#050608;
    --brand-blue:#1a4ea0;
    --band-blue:#0d4596;
    --deep-navy:#0b2454;
    --mid-navy:#123773;
    --name-blue:#1d4f9e;
    --white:#ffffff;
    --muted-blue:#8fb2e6;
  }
  *{box-sizing:border-box;margin:0;padding:0}
  html,body{width:1200px;height:891px;overflow:hidden;background:var(--page)}
  .canvas{position:relative;width:1200px;height:891px}
  .card{position:absolute;width:520px;height:298px;background:var(--card-black);overflow:hidden;
        box-shadow:0 10px 28px rgba(0,0,0,.25)}
  .card--front{left:50px;top:296px}
  .card--back{left:630px;top:296px}

  /* front */
  .brand-dot{position:absolute;left:56px;top:76px;width:112px;height:112px;border-radius:50%;
             background:radial-gradient(circle at 40% 35%,#2b6fd0,var(--band-blue) 70%)}
  .brand-name{position:absolute;left:190px;top:88px;font-family:"Lato",sans-serif;font-weight:300;
              font-size:50px;letter-spacing:1px;color:var(--brand-blue);line-height:1;white-space:nowrap}
  .brand-rule{position:absolute;left:190px;top:150px;width:290px;height:2px;background:var(--brand-blue)}
  .brand-tagline{position:absolute;left:192px;top:158px;font-family:"Lato",sans-serif;font-weight:400;
                 font-size:16px;letter-spacing:.5px;color:var(--brand-blue);white-space:nowrap}
  .card-band{position:absolute;left:0;right:0;bottom:0;height:38px;background:var(--band-blue)}
  .card--front .card-band::before{content:"";position:absolute;left:0;right:0;top:0;height:5px;background:#0a3578}

  /* back */
  .back-art{position:absolute;left:0;top:0}
  .maker-list{position:absolute;left:26px;top:70px;display:grid;grid-template-columns:auto auto;gap:14px 20px;
              font-family:"Lato",sans-serif;font-weight:700;font-size:12px;letter-spacing:1px;color:var(--white)}
  .maker{display:flex;align-items:center;gap:6px;text-transform:uppercase}
  .maker::before{content:"";width:10px;height:10px;border-radius:50%;background:var(--muted-blue)}
  .back-name{position:absolute;left:292px;top:94px;font-family:"Lato",sans-serif;font-weight:300;
             font-size:38px;color:var(--name-blue);line-height:1;white-space:nowrap}
  .back-rule{position:absolute;left:292px;top:140px;width:204px;height:2px;background:var(--name-blue)}
  .back-tagline{position:absolute;left:293px;top:146px;font-family:"Lato",sans-serif;font-size:13px;
                color:var(--name-blue);white-space:nowrap}
  .contact-list{position:absolute;left:300px;top:178px;list-style:none;font-family:"Arimo",sans-serif;
                font-size:15px;color:var(--white)}
  .contact-list li{display:flex;align-items:center;gap:10px;height:24px}
  .contact-list svg{width:16px;height:16px;flex:none}
  .card--back .card-band{display:flex;align-items:center;gap:10px;padding-left:22px;
                         font-family:"Arimo",sans-serif;font-size:16px;color:var(--white)}
  .card--back .card-band svg{width:16px;height:20px}
</style>
</head>
<body>
<main class="canvas">

  <section class="card card--front" aria-label="Business card front">
    <div class="brand-dot"></div>
    <div class="brand-name">RK HALDEN</div>
    <div class="brand-rule"></div>
    <div class="brand-tagline">ACCIDENT REPAIR CENTRE</div>
    <div class="card-band"></div>
  </section>

  <section class="card card--back" aria-label="Business card back">
    <svg class="back-art" width="520" height="298" viewBox="0 0 520 298" aria-hidden="true">
      <rect x="0" y="0" width="250" height="260" fill="var(--deep-navy)"/>
      <circle cx="150" cy="30" r="125" fill="var(--mid-navy)"/>
      <circle cx="70" cy="-10" r="100" fill="#0f2f66"/>
    </svg>
    <div class="maker-list">
      <span class="maker">Orek</span>
      <span class="maker">Tovalo</span>
      <span class="maker">Velmora</span>
      <span class="maker">Kestrel</span>
      <span class="maker">Sorami</span>
    </div>
    <div class="back-name">RK HALDEN</div>
    <div class="back-rule"></div>
    <div class="back-tagline">ACCIDENT REPAIR CENTRE</div>
    <ul class="contact-list">
      <li><svg viewBox="0 0 16 16"><path d="M4 1 l3 3 -2 2 c1 2 3 4 5 5 l2-2 3 3 -2 2 C7 14 2 9 2 3z" fill="var(--white)"/></svg>Contact Number</li>
      <li><svg viewBox="0 0 16 16"><rect x="1" y="3" width="14" height="10" fill="var(--white)"/><path d="M1 3 L8 9 L15 3" stroke="var(--card-black)" stroke-width="1.2" fill="none"/></svg>Email</li>
      <li><svg viewBox="0 0 16 16" fill="none" stroke="var(--white)" stroke-width="1.2"><circle cx="8" cy="8" r="6.5"/><ellipse cx="8" cy="8" rx="3" ry="6.5"/><path d="M1.5 8h13M2.5 4.8h11M2.5 11.2h11"/></svg>Web address</li>
    </ul>
    <div class="card-band">
      <svg viewBox="0 0 16 20"><path d="M8 0 C3.6 0 1 3.2 1 7 C1 12 8 20 8 20 S15 12 15 7 C15 3.2 12.4 0 8 0z" fill="var(--white)"/><circle cx="8" cy="7" r="2.6" fill="var(--band-blue)"/></svg>
      Street Address
    </div>
  </section>

</main>
</body>
</html>
```